Automotive Accessories Business Card

Design a business template that match our new logo design and our industry.

https://www.kelvramotive.com/

Target Market(s)

Aftermarket auto parts and accessories

Industry/Entity Type

automotive

Contact Information for Business Card

company logo

Font styles to use
Serif
Sans Serif

Colors
EB3D1F
EC4F4E
F09395
F8D3D4
FCEDEE

```html
<!DOCTYPE html>
<html lang="en">
<head>
<meta charset="utf-8">
<title>Kelvra Motive Inc — Business Card</title>
<link rel="stylesheet" href="https://fonts.googleapis.com/css2?family=Montserrat:wght@400;500;700&display=swap">
<style>
  :root {
    --red: #d71f27;
    --charcoal: #38383a;
    --ink: #1d1d1f;
    --card-white: #ffffff;
    --card-black: #1e1e20;
    --card-black-2: #2a2a2c;
    --canvas: #d9d9d9;
    --rule: #8a8a8a;
  }
  * { box-sizing: border-box; margin: 0; padding: 0; }
  html, body { width: 1200px; height: 1200px; overflow: hidden; }
  body {
    background: var(--canvas);
    font-family: "Montserrat", Arial, sans-serif;
    position: relative;
  }
  .card {
    position: absolute;
    left: 150px;
    width: 900px;
    height: 514px;
    border-radius: 28px;
    overflow: hidden;
    box-shadow: 0 10px 28px rgba(0,0,0,.25);
  }
  /* Front */
  .card-front { top: 60px; background: var(--card-white); }
  .front-logo {
    position: absolute; left: 210px; top: 120px;
    display: flex; align-items: center; gap: 14px;
  }
  .logo-mark { width: 26px; height: 26px; background: var(--red); }
  .logo-name {
    font-weight: 700; font-size: 38px; letter-spacing: 2px;
    color: var(--red); text-transform: uppercase; white-space: nowrap;
  }
  .divider {
    position: absolute; left: 512px; top: 210px;
    width: 1px; height: 150px; background: var(--rule);
  }
  .person {
    position: absolute; left: 580px; top: 238px;
    padding-left: 20px; border-left: 6px solid var(--red);
  }
  .person-name {
    font-weight: 500; font-size: 36px; color: var(--red);
    text-transform: uppercase; line-height: 1.05;
  }
  .person-role {
    font-weight: 500; font-size: 17px; color: var(--ink);
    text-transform: uppercase; letter-spacing: .5px; margin-top: 4px;
  }
  .contact {
    position: absolute; left: 100px; top: 296px;
    list-style: none; font-size: 16px; color: var(--ink); line-height: 1.3;
  }
  .contact li { display: flex; align-items: flex-start; gap: 12px; margin-bottom: 3px; }
  .contact svg { width: 16px; height: 16px; flex: none; margin-top: 2px; fill: var(--red); }
  .band-red {
    position: absolute; left: 0; bottom: 0; width: 596px; height: 26px; background: var(--red);
  }
  .band-dark {
    position: absolute; right: 0; bottom: 0; width: 300px; height: 44px; background: var(--charcoal);
  }
  /* Back */
  .card-back {
    top: 626px;
    background: radial-gradient(ellipse at 50% 45%, var(--card-black-2), var(--card-black) 75%);
  }
  .back-texture { position: absolute; inset: 0; }
  .back-logo {
    position: absolute; left: 0; right: 0; top: 0; bottom: 0;
    display: flex; align-items: center; justify-content: center; gap: 20px;
  }
  .back-logo .logo-mark { width: 36px; height: 36px; }
  .back-logo .logo-name { color: #ffffff; font-size: 56px; letter-spacing: 3px; }
</style>
</head>
<body>
  <section class="card card-front">
    <div class="front-logo">
      <span class="logo-mark"></span>
      <span class="logo-name">Kelvra Motive Inc</span>
    </div>
    <div class="divider"></div>
    <div class="person">
      <div class="person-name">Dana Reyes</div>
      <div class="person-role">Manager</div>
    </div>
    <ul class="contact">
      <li><svg viewBox="0 0 16 16"><path d="M3.5 1.5l2.5 0 1 3.5-1.7 1.2a8 8 0 0 0 4.5 4.5L11 9l3.5 1v2.5c0 1-1 2-2 2A11 11 0 0 1 1.5 3.5c0-1 1-2 2-2z"/></svg>+1-555-014-2290</li>
      <li><svg viewBox="0 0 16 16"><path d="M1 3h14v10H1z M1.5 3.5L8 9l6.5-5.5" stroke="#fff" stroke-width="1.2"/></svg>sales@kelvramotive.com</li>
      <li><svg viewBox="0 0 16 16"><circle cx="8" cy="8" r="7"/><path d="M1 8h14M8 1c-3 3-3 11 0 14M8 1c3 3 3 11 0 14" stroke="#fff" stroke-width="1" fill="none"/></svg>www.kelvramotive.com</li>
      <li><svg viewBox="0 0 16 16"><path d="M8 1a5 5 0 0 1 5 5c0 4-5 9-5 9S3 10 3 6a5 5 0 0 1 5-5z"/><circle cx="8" cy="6" r="2" fill="#fff"/></svg><span>418 Linden Ave. Unit C<br>Millbrook, CA, 91700 United States</span></li>
    </ul>
    <div class="band-red"></div>
    <div class="band-dark"></div>
  </section>

  <section class="card card-back">
    <div class="back-texture" role="img" aria-label="Subtle dark honeycomb texture across the card"></div>
    <div class="back-logo">
      <span class="logo-mark"></span>
      <span class="logo-name">Kelvra Motive Inc</span>
    </div>
  </section>
</body>
</html>
```